High-end residential home builder needs a business card design

We need a new business card design for a small residential construction company based in Boise, Idaho. We specialize in building custom high-end homes and remodels, with a focus on great design and craftsmanship.

We would like to use our current logo, but open to new color suggestions.
Just looking for a clean, sharp, modern design that looks high-end.

Target Market(s)

Upscale clientele

Industry/Entity Type

Contractor

Contact Information for Business Card

Company: Stonefield Custom Builders
Name: Marcus Tilley
Phone number: 208 367 4120
Email: MarcusTilleySCB@mailbox-example.com
Website: Stonefieldcustombuilders-example.com

Font styles to use
Serif
Sans Serif

Requirements
Must have
• Company Logo
Company name
My name
My phone number
My email
Company website
Nice to have
• I have attached a few photos of cards that I really like.

```html
<!DOCTYPE html>
<html lang="en">
<head>
<meta charset="utf-8">
<title>Stonefield Custom Builders – Business Card</title>
<link href="https://fonts.googleapis.com/css2?family=Raleway:wght@500;600&family=Roboto:wght@400;700&display=swap" rel="stylesheet">
<style>
  :root {
    --backdrop: #e4e4e4;
    --ink: #0b0b0b;
    --brown: #2a1409;
    --orange: #f0901c;
    --paper: #ffffff;
    --text-dark: #1c120c;
  }
  * { margin: 0; padding: 0; box-sizing: border-box; }
  html, body { width: 1200px; height: 800px; overflow: hidden; }
  body {
    background: var(--backdrop);
    font-family: "Roboto", Arial, sans-serif;
    position: relative;
  }
  .card {
    position: absolute;
    top: 252px;
    width: 520px;
    height: 297px;
    border-radius: 4px;
    overflow: hidden;
    box-shadow: 0 6px 18px rgba(0,0,0,0.18);
  }
  /* Front side */
  .card-front { left: 50px; background: var(--ink); }
  .front-brand {
    position: absolute;
    left: 0; right: 0; top: 62px;
    display: flex; flex-direction: column; align-items: center;
  }
  .brand-mark {
    width: 74px; height: 74px;
    border: 2px solid var(--paper);
    margin-bottom: 26px;
  }
  .front-name {
    font-family: "Raleway", Arial, sans-serif;
    font-weight: 600;
    font-size: 25px;
    letter-spacing: 7px;
    text-transform: uppercase;
    color: var(--paper);
    text-align: center;
    line-height: 1.45;
  }
  .front-name .line2 { display: block; font-size: 17px; letter-spacing: 6px; }

  /* Back side */
  .card-back { left: 630px; background: var(--paper); }
  .back-header {
    position: absolute; top: 22px; right: 26px;
    text-align: right;
    font-family: "Raleway", Arial, sans-serif;
    font-weight: 600;
    font-size: 23px;
    letter-spacing: 6px;
    text-transform: uppercase;
    color: var(--text-dark);
    line-height: 1.35;
  }
  .back-header .line2 { display: block; font-size: 15px; letter-spacing: 5px; }
  .person { position: absolute; left: 34px; top: 98px; }
  .person-name { font-weight: 700; font-size: 19px; color: var(--text-dark); }
  .person-role { font-size: 13px; color: var(--orange); margin-top: 2px; }
  .person-rule { width: 24px; height: 2px; background: var(--text-dark); margin-top: 6px; }
  .contact-list { position: absolute; left: 34px; top: 165px; list-style: none; }
  .contact-list li {
    display: flex; align-items: center; gap: 8px;
    font-size: 12.5px; color: var(--text-dark); margin-bottom: 6px;
  }
  .contact-list svg { width: 11px; height: 11px; fill: var(--orange); flex: none; }
  .back-swoosh { position: absolute; left: 0; bottom: 0; width: 520px; height: 297px; }
</style>
</head>
<body>

<section class="card card-front" aria-label="Card front">
  <div class="front-brand">
    <div class="brand-mark"></div>
    <p class="front-name">Stonefield<span class="line2">Custom Builders</span></p>
  </div>
</section>

<section class="card card-back" aria-label="Card back">
  <svg class="back-swoosh" viewBox="0 0 520 297" preserveAspectRatio="none" aria-hidden="true">
    <defs>
      <linearGradient id="bandShade" x1="0" x2="1" y1="0" y2="0">
        <stop offset="0" stop-color="#120804"/>
        <stop offset="1" stop-color="#3a1c08"/>
      </linearGradient>
    </defs>
    <path d="M0 236 C150 226 330 250 520 224 L520 297 L0 297 Z" fill="var(--orange)"/>
    <path d="M0 243 C150 234 330 258 520 232 L520 297 L0 297 Z" fill="var(--paper)"/>
    <path d="M0 249 C150 241 330 264 520 238 L520 297 L0 297 Z" fill="url(#bandShade)"/>
  </svg>

  <p class="back-header">Stonefield<span class="line2">Custom Builders</span></p>

  <div class="person">
    <p class="person-name">Marcus Tilley</p>
    <p class="person-role">CEO</p>
    <div class="person-rule"></div>
  </div>

  <ul class="contact-list">
    <li><svg viewBox="0 0 24 24"><path d="M6.6 10.8a15.1 15.1 0 0 0 6.6 6.6l2.2-2.2a1 1 0 0 1 1-.25 11.4 11.4 0 0 0 3.6.57 1 1 0 0 1 1 1V20a1 1 0 0 1-1 1A17 17 0 0 1 3 4a1 1 0 0 1 1-1h3.5a1 1 0 0 1 1 1c0 1.25.2 2.45.57 3.57a1 1 0 0 1-.25 1z"/></svg>208 367 4120</li>
    <li><svg viewBox="0 0 24 24"><path d="M2 5h20v14H2z M2 5l10 8 10-8" /></svg>MarcusTilleySCB@mailbox-example.com</li>
    <li><svg viewBox="0 0 24 24"><circle cx="12" cy="12" r="10"/></svg>Stonefieldcustombuilders-example.com</li>
  </ul>
</section>

</body>
</html>
```